Updated Business Card Design more modern and eye catching

looking for something more dynamic than the sterile card we have now. Please take a look at our web site www.brindlemarket.net to see what we do. only looking for the front side of the card for now. I've also attached a sample of a card with raised spot uv ink - it might be cool to incorporate something like that. Card should be bold yet serious. No frilly or scrolly stuff on it.
Updates
Target Market(s)
We do decor and signage for retail business and supermarkets. Our new name should reflect that we're hip but serious.
Contact Information for Business Card
standard business card size - horizontal preferred
Font styles to use
Requirements
Must have
- Current logo and colors cannot be changed.
Nice to have
- Must have information shown on existing card but open to some changes. Okay to consider spot uv.
Should not have
- Not busy with pictures in the background.

```html
<!DOCTYPE html>
<html lang="en">
<head>
<meta charset="utf-8">
<title>Brindle Market – Business Card</title>
<link href="https://fonts.googleapis.com/css2?family=Montserrat:wght@400;500;600;700;800&display=swap" rel="stylesheet">
<style>
  :root {
    --page-bg: #d9dbde;
    --card-white: #ffffff;
    --card-black: #0b0b0b;
    --gold: #b9a951;
    --gold-shadow: #8a7c33;
    --ink: #1a1a1a;
    --text-light: #ffffff;
  }
  * { margin: 0; padding: 0; box-sizing: border-box; }
  html, body {
    width: 1200px; height: 675px; overflow: hidden;
    background: var(--page-bg);
    font-family: "Montserrat", sans-serif;
  }
  .stage {
    width: 1200px; height: 675px;
    display: flex; align-items: center; justify-content: center;
  }
  .card {
    position: relative;
    width: 910px; height: 520px;
    background: var(--card-white);
    overflow: hidden;
    box-shadow: 0 10px 30px rgba(0,0,0,0.18);
  }
  .card-shapes { position: absolute; inset: 0; width: 100%; height: 100%; }

  .brand {
    position: absolute; left: 90px; top: 228px;
    display: flex; align-items: center; gap: 16px;
  }
  .brand-square {
    width: 42px; height: 42px; background: var(--gold);
  }
  .brand-name {
    font-weight: 700; font-size: 34px; letter-spacing: 3px;
    color: var(--ink); text-transform: uppercase;
  }

  .nameplate {
    position: absolute; left: 560px; top: 104px;
    width: 330px; text-align: center; color: var(--ink);
  }
  .person-name {
    font-weight: 800; font-size: 30px; letter-spacing: 1px; line-height: 1;
  }
  .person-title {
    margin-top: 4px; text-align: right; padding-right: 18px;
    font-weight: 600; font-size: 11px; letter-spacing: 3px;
  }

  .contact-list {
    position: absolute; left: 560px; top: 216px;
    list-style: none; color: var(--text-light);
  }
  .contact-item {
    display: flex; align-items: flex-start; gap: 14px;
    font-weight: 500; font-size: 19px; line-height: 1.3;
    margin-bottom: 11px;
  }
  .contact-icon {
    flex: 0 0 28px; width: 28px; height: 28px; margin-top: -1px;
  }
</style>
</head>
<body>
<main class="stage">
  <article class="card">
    <svg class="card-shapes" viewBox="0 0 910 520" aria-hidden="true">
      <polygon points="450,0 910,0 910,520 590,520" fill="var(--card-black)"/>
      <polygon points="510,130 540,130 540,158" fill="var(--gold-shadow)"/>
      <polygon points="470,80 910,80 910,158 510,158 510,130" fill="var(--gold)"/>
    </svg>

    <div class="brand">
      <span class="brand-square"></span>
      <span class="brand-name">Brindle Market</span>
    </div>

    <header class="nameplate">
      <h1 class="person-name">MARLA QUINN</h1>
      <p class="person-title">VICE PRESIDENT</p>
    </header>

    <ul class="contact-list">
      <li class="contact-item">
        <svg class="contact-icon" viewBox="0 0 28 28" aria-hidden="true"><circle cx="14" cy="14" r="13" fill="#fff"/><rect x="10" y="6.5" width="8" height="15" rx="1.5" fill="none" stroke="#0b0b0b" stroke-width="1.8"/><circle cx="14" cy="18.5" r="1" fill="#0b0b0b"/></svg>
        <span>555.210.4837</span>
      </li>
      <li class="contact-item">
        <svg class="contact-icon" viewBox="0 0 28 28" aria-hidden="true"><circle cx="14" cy="14" r="13" fill="#fff"/><path d="M9 7.5l3 .2 1.2 3.6-1.8 1.4a9 9 0 0 0 4 4l1.4-1.8 3.6 1.2.2 3a2 2 0 0 1-2.2 1.8A12 12 0 0 1 7.3 9.7 2 2 0 0 1 9 7.5z" fill="#0b0b0b"/></svg>
        <span>555.318.6620 ext.3</span>
      </li>
      <li class="contact-item">
        <svg class="contact-icon" viewBox="0 0 28 28" aria-hidden="true"><circle cx="14" cy="14" r="13" fill="#fff"/><rect x="7.5" y="9.5" width="13" height="9" fill="#0b0b0b"/><path d="M7.5 9.5l6.5 5 6.5-5" fill="none" stroke="#fff" stroke-width="1.2"/></svg>
        <span>marla@BrindleMarket.net</span>
      </li>
      <li class="contact-item">
        <svg class="contact-icon" viewBox="0 0 28 28" aria-hidden="true"><circle cx="14" cy="14" r="13" fill="#fff"/><g fill="none" stroke="#0b0b0b" stroke-width="1.5"><circle cx="14" cy="14" r="7"/><ellipse cx="14" cy="14" rx="3" ry="7"/><path d="M7 14h14M8 10.5h12M8 17.5h12"/></g></svg>
        <span>www.BrindleMarket.net</span>
      </li>
      <li class="contact-item">
        <svg class="contact-icon" viewBox="0 0 28 28" aria-hidden="true"><circle cx="14" cy="14" r="13" fill="#fff"/><path d="M14 6.5a5.5 5.5 0 0 0-5.5 5.5c0 4 5.5 10 5.5 10s5.5-6 5.5-10A5.5 5.5 0 0 0 14 6.5z" fill="#0b0b0b"/><circle cx="14" cy="12" r="2" fill="#fff"/></svg>
        <span>410 Harbor Commerce<br>Way, Fort Wrenn,<br>FL 30418</span>
      </li>
    </ul>
  </article>
</main>
</body>
</html>
```